Bewertungskarte für ein Bauunternehmen
Zielgruppe
Wir sind ein junges Bauunternehmen und machen schlüsselfertigen Einfamilienhausbau sowie Altbausanierungen.
Unsere Zielgruppe sind junge Familien und generell Menschen im Alter zwischen 20 und 55 Jahren.
Aufgabenstellung
Wir wollen eine Bewertungskarte für unser Unternehmen erstellen. Es soll hier ein QR-Code drauf sein, wo man direkt zur fundix-Bewertung unseres Unternehmens kommt.
Die Karte soll beidseitig bedruckt sein. Ein Umschlag ist nicht notwendig. Briefkartenformat könnten wir uns gut vorstellen. Für andere Anregungen sind wir offen.
Wir haben Beispielkarten anderer Unternehmen beigefügt. Daran können Sie sich orientieren.

```html
<!DOCTYPE html>
<html lang="de">
<head>
<meta charset="utf-8">
<title>Bewertungskarte – kernbau</title>
<link href="https://fonts.googleapis.com/css2?family=Nunito:wght@300;900&display=swap" rel="stylesheet">
<style>
  :root {
    --card-grey: #c6c5c7;
    --brand-red: #8f2020;
    --white: #ffffff;
    --photo-light: #d9d6d0;
    --photo-warm: #c7a57c;
  }
  html, body {
    margin: 0;
    padding: 0;
    width: 1200px;
    height: 851px;
    overflow: hidden;
  }
  .card {
    position: relative;
    width: 1200px;
    height: 851px;
    background: var(--card-grey);
    font-family: "Nunito", sans-serif;
    overflow: hidden;
  }
  .brand {
    position: absolute;
    left: 103px;
    top: 100px;
    display: flex;
    align-items: center;
    gap: 10px;
    font-size: 50px;
    font-weight: 900;
    line-height: 1;
    color: var(--brand-red);
    letter-spacing: -1px;
  }
  .brand__mark {
    width: 14px;
    height: 14px;
    background: var(--brand-red);
  }
  .intro {
    position: absolute;
    left: 103px;
    top: 280px;
    margin: 0;
    font-size: 46px;
    font-weight: 300;
    color: var(--white);
    letter-spacing: 0.5px;
  }
  .headline {
    position: absolute;
    left: 102px;
    top: 340px;
    margin: 0;
    font-size: 101px;
    font-weight: 900;
    line-height: 112px;
    color: var(--brand-red);
    letter-spacing: -1px;
    z-index: 2;
  }
  .brush-stroke {
    position: absolute;
    left: 51px;
    top: 540px;
    width: 724px;
    height: 34px;
    z-index: 1;
  }
  .chat-panel {
    position: absolute;
    left: 822px;
    top: 0;
    width: 378px;
    height: 425px;
    background: var(--brand-red);
  }
  .chat-icon {
    position: absolute;
    left: 0;
    top: 0;
  }
  .team-photo {
    position: absolute;
    left: 822px;
    top: 425px;
    width: 378px;
    height: 426px;
    background: linear-gradient(135deg, var(--photo-light) 0%, #bdb8b0 45%, var(--photo-warm) 100%);
  }
</style>
</head>
<body>
<main class="card">
  <div class="brand"><span class="brand__mark"></span>kernbau</div>

  <p class="intro">SAGEN SIE UNS MAL</p>
  <h1 class="headline">SO RICHTIG<br>DIE MEINUNG</h1>

  <svg class="brush-stroke" viewBox="0 0 724 34" preserveAspectRatio="none" aria-hidden="true">
    <path d="M4 8 L60 5 L140 6 L230 3 L330 5 L430 2 L530 4 L620 1 L722 3 L720 14 L716 27 L640 29 L540 28 L440 31 L340 29 L240 32 L140 30 L40 32 L6 30 L8 20 L0 14 Z" fill="#ffffff"/>
  </svg>

  <section class="chat-panel">
    <svg class="chat-icon" width="378" height="425" viewBox="0 0 378 425" aria-hidden="true"
         fill="none" stroke="#ffffff" stroke-width="7" stroke-linecap="round" stroke-linejoin="round">
      <path d="M189 120 C250 120 290 155 290 200 C290 245 250 280 189 280 C175 280 162 278 150 275 L110 300 L120 262 C99 247 88 225 88 200 C88 155 128 120 189 120 Z"/>
      <line x1="140" y1="180" x2="238" y2="180"/>
      <line x1="140" y1="202" x2="238" y2="202"/>
      <line x1="140" y1="224" x2="205" y2="224"/>
    </svg>
  </section>

  <div class="team-photo" role="img" aria-label="Foto eines lächelnden Handwerkers in Arbeitsweste auf der Baustelle"></div>
</main>
</body>
</html>
```